Family business needs stationery redesign with new logo

Family owned company, established in 1987 wanting a brand 'refresh'. We are an electrical, refrigeration and construction company based in the Barkly Region Northern Territory, Australia. We have a new logo we would like to use which is uploaded along with our current letterhead and email signature. We are also dropping the word 'contractors' so please do not include this on any designs. Please note also, the 'orange' color used in our logo and designs should be Northern Territory red ochre which is as follows:

RGB (Hex): #C75B12
PantoneĀ® 159 C
CMYK: 1 / 74 / 100 / 7

We are needing our stationery redesigned using our new logo. Please include letterheads, business cards, envelopes, and email signatures.

We currently use our business letterheads for quotations, invoices, letters, HR matters, and internal memos.

We also need a separate simplified letterhead for internal paperwork such as employee leave forms, meeting agendas, and meeting minutes etc.
Updates

Reason: Needing more submissions of full package designs. We are wanting all our stationery, including business cards, letterheads, email signatures, envelopes, etc to be cohesive. We also require ALL the information, as supplied on our template letterhead, to be included on the new letterhead designs. including electrical license no.etc Thank you, K&M

Reason: needing more time as work has got in the way of looking over designs. A lot of designs not meeting the brief/criteria.

Industry/Entity Type

Business

Colors
0355a3
f37122

Requirements
Must have
• The 'orange' color used in the designs should be Northern Territory red ochre which is as follows:
• RGB (Hex): #C75B12
• PantoneĀ® 159 C
• CMYK: 1 / 74 / 100 / 7
• ***MUST INCLUDE ALL INFORMATION THAT IS ON OUR CURRENT LETTERHEAD***
Should not have
• Please do not include the word 'contractors'

```html
<!DOCTYPE html>
<html lang="en">
<head>
<meta charset="utf-8">
<title>K&amp;M Stationery Suite</title>
<link rel="stylesheet" href="https://fonts.googleapis.com/css2?family=Source+Sans+3:wght@400;600;700&display=swap">
<style>
  :root {
    --backdrop: #939598;
    --navy: #23326c;
    --ochre: #c75b12;
    --paper: #ffffff;
    --ink-grey: #7a7a7a;
    --charcoal: #3b3b3d;
    --rule: #9a9a9a;
  }
  html, body { margin: 0; padding: 0; width: 1200px; height: 1200px; overflow: hidden; background: var(--backdrop); }
  svg.suite { display: block; width: 1200px; height: 1200px; font-family: "Source Sans 3", sans-serif; }
  .paper { fill: var(--paper); }
  .navy { fill: var(--navy); }
  .charcoal { fill: var(--charcoal); }
  .ochre-line { fill: none; stroke: var(--ochre); stroke-width: 2.5; }
  .mark { fill: var(--navy); font-weight: 700; }
  .mark-light { fill: var(--paper); font-weight: 700; }
  .tag { fill: var(--navy); font-weight: 700; font-size: 5px; }
  .tag-light { fill: var(--paper); font-weight: 700; }
  .addr-h { fill: var(--navy); font-weight: 700; font-size: 8px; }
  .addr { fill: var(--navy); font-weight: 600; font-size: 5px; }
  .addr-light { fill: var(--paper); font-weight: 600; }
  .icon { fill: none; stroke: var(--navy); stroke-width: 0.8; }
  .icon-light { fill: none; stroke: var(--paper); stroke-width: 0.8; }
  .ghost { fill: var(--navy); opacity: 0.05; font-weight: 700; }
  .ghost-light { fill: var(--paper); opacity: 0.06; font-weight: 700; }
  .foot-text { fill: var(--paper); font-size: 4.8px; font-weight: 600; }
  .doc-title { fill: var(--navy); font-weight: 700; font-size: 11.5px; }
  .label { fill: var(--navy); font-weight: 700; font-size: 8.5px; }
  .value { fill: var(--ink-grey); font-size: 8.5px; }
  .body-small { fill: var(--ink-grey); font-size: 6.6px; }
  .letter-text { fill: var(--ink-grey); font-size: 5px; }
  .letter-bold { fill: #555; font-size: 5px; font-weight: 700; }
  .cell { fill: none; stroke: var(--rule); stroke-width: 0.6; }
  .cell-text { fill: #555; font-size: 4.4px; }
  .bar-text { fill: var(--paper); font-size: 4.6px; }
  .faint-line { fill: none; stroke: #e4e4e4; stroke-width: 1.2; }
  .signature-area { fill: #ececec; }
</style>
</head>
<body>
<svg class="suite" viewBox="0 0 1500 1500" xmlns="http://www.w3.org/2000/svg" xmlns:xlink="http://www.w3.org/1999/xlink">
  <defs>
    <g id="sheet-head">
      <text class="mark" x="25" y="61" font-size="24">K&amp;M</text>
      <text class="tag"><tspan x="93" y="46">Electrical</tspan><tspan x="93" y="53">Refrigeration</tspan><tspan x="93" y="60">Building Services</tspan></text>
      <text class="addr-h" x="244" y="25">Address :</text>
      <text class="addr"><tspan x="244" y="33">42 Ridge Rd, PO Box 310,</tspan><tspan x="244" y="40">Red Gum NT. 0870</tspan></text>
      <rect class="icon" x="245" y="48" width="3.5" height="6" rx="0.6"/>
      <text class="addr" x="257" y="54">Ph: 08 8100 2345</text>
      <rect class="navy" x="244.5" y="60" width="6" height="5"/>
      <text class="addr" x="257" y="65">Fax: 08 8100 2346</text>
      <rect class="icon" x="244.5" y="72" width="7" height="5"/>
      <polyline class="icon" points="244.5,72 248,75 251.5,72"/>
      <text class="addr" x="257" y="77">info@km.com.au</text>
    </g>
    <g id="sheet-foot">
      <path class="ochre-line" d="M0,401 C110,440 230,456 338,460"/>
      <path class="navy" d="M0,409 C110,448 230,463 338,465 L338,478 L0,478 Z"/>
      <text class="foot-text"><tspan x="26" y="453">ABN 12 34 56 78</tspan><tspan x="26" y="461">Refrigerant Trading Authorisation ABCDEFG</tspan><tspan x="26" y="469">NT Electrical Contractors License 1234</tspan></text>
    </g>
    <g id="sheet-ghost">
      <text class="ghost" x="169" y="350" font-size="110" text-anchor="middle">K&amp;M</text>
    </g>
    <g id="agenda-body">
      <text class="label"><tspan x="26" y="142">Purpose :</tspan><tspan x="26" y="156">Date</tspan><tspan x="26" y="170">Place</tspan><tspan x="26" y="184">Time</tspan></text>
      <text class="label"><tspan x="66" y="156">:</tspan><tspan x="66" y="170">:</tspan><tspan x="66" y="184">:</tspan></text>
      <text class="value"><tspan x="117" y="142">Lorem ipsum dolor sit</tspan><tspan x="117" y="156">Lorem ipsum dolor sit</tspan><tspan x="117" y="170">Lorem ipsum dolor sit</tspan><tspan x="117" y="184">Lorem ipsum dolor sit</tspan></text>
      <text class="label" x="26" y="212">Attendees:</text>
      <text class="body-small"><tspan x="78" y="212">Lorem ipsum dolor sit amet, consectetur adipiscing elit, sed do</tspan><tspan x="40" y="221">eiusmod tempor incididunt ut labore et dolore magna aliqua. Ut enim ad</tspan><tspan x="40" y="230">minim veniam, quis nostrud exercitation ullamco laboris nisi ut aliquip ex ea</tspan><tspan x="40" y="239">commodo consequat.</tspan></text>
      <text class="label"><tspan x="26" y="260">Topic</tspan><tspan x="153" y="260">Presenter</tspan><tspan x="264" y="260">Time</tspan></text>
      <text class="value"><tspan x="26" y="274">Lorem ipsum dolor</tspan><tspan x="26" y="287">Lorem ipsum dolor</tspan><tspan x="26" y="301">Lorem ipsum dolor</tspan><tspan x="26" y="315">Lorem ipsum dolor</tspan></text>
      <text class="value"><tspan x="153" y="274">ABC</tspan><tspan x="153" y="287">ABC</tspan><tspan x="153" y="301">ABC</tspan><tspan x="153" y="315">ABC</tspan></text>
      <text class="value"><tspan x="261" y="274">12:00 - 3:00</tspan><tspan x="261" y="287">12:00 - 3:00</tspan><tspan x="261" y="301">12:00 - 3:00</tspan><tspan x="261" y="315">12:00 - 3:00</tspan></text>
      <text class="label" x="26" y="370">Additional information:</text>
      <text class="body-small" x="26" y="380">Lorem ipsum dolor sit amet, consectetur adipiscing elit, sed do</text>
    </g>
    <clipPath id="disc-clip"><circle cx="222" cy="1315" r="147"/></clipPath>
  </defs>

  <!-- Agenda letterhead -->
  <g class="sheet agenda-sheet" transform="translate(34 35)">
    <rect class="paper" width="338" height="478"/>
    <use href="#sheet-ghost"/>
    <use href="#sheet-head"/>
    <text class="doc-title" x="26" y="120">MEETING AGENDA</text>
    <use href="#agenda-body"/>
    <use href="#sheet-foot"/>
  </g>

  <!-- Business letterhead -->
  <g class="sheet letter-sheet" transform="translate(424 35)">
    <rect class="paper" width="338" height="478"/>
    <use href="#sheet-ghost"/>
    <use href="#sheet-head"/>
    <text class="letter-text" x="26" y="118">Date</text>
    <text class="letter-bold" x="26" y="134">Recipient Name</text>
    <text class="letter-text"><tspan x="26" y="151">Company Name</tspan><tspan x="26" y="159">Street Adress</tspan><tspan x="26" y="167">City, State, Zip</tspan></text>
    <text class="letter-text">
      <tspan x="26" y="182">Thank you for the chance to quote on the upgrade works at your site this month.</tspan>
      <tspan x="26" y="190">Our team has reviewed the plans and prepared a full scope for the electrical work.</tspan>
      <tspan x="26" y="198">Pricing covers labour, parts and testing, with all works carried out to standard.</tspan>
      <tspan x="26" y="206">Please read the attached details and contact our office with any questions.</tspan>
      <tspan x="26" y="236">Refrigeration service will be booked in line with your preferred dates and hours.</tspan>
      <tspan x="26" y="244">A site visit can be arranged before work starts to confirm access and safety.</tspan>
      <tspan x="26" y="252">All staff hold current licences and carry full insurance for each job we take.</tspan>
      <tspan x="26" y="260">We will keep you updated at every stage until the work is signed off.</tspan>
      <tspan x="26" y="277">Building services include repairs, fit-outs and routine maintenance on request.</tspan>
      <tspan x="26" y="285">Our crews are based locally and can respond quickly across the whole region.</tspan>
      <tspan x="26" y="293">Invoices are issued on completion with payment terms shown on the quote.</tspan>
      <tspan x="26" y="301">We value your business and look forward to working with you again soon.</tspan>
      <tspan x="26" y="318">Should your plans change, simply let us know and we will adjust the schedule.</tspan>
      <tspan x="26" y="326">Thank you again for choosing a family business that has served the area for years.</tspan>
      <tspan x="26" y="334">Kind regards from all of us.</tspan>
      <tspan x="26" y="357">Sincerely</tspan>
    </text>
    <rect class="signature-area" x="32" y="363" width="80" height="22" role="img" aria-label="Handwritten signature"/>
    <text class="mark" x="86" y="398" font-size="10">Sam K &amp; M</text>
    <text class="letter-text" x="86" y="405" font-size="4">CORPORATE SERVICES MANAGER</text>
    <use href="#sheet-foot"/>
  </g>

  <!-- DL envelope front -->
  <g class="envelope-dl" transform="translate(823 36)">
    <rect class="paper" width="589" height="257"/>
    <text class="ghost" x="440" y="150" font-size="120" text-anchor="middle">K&amp;M</text>
    <text class="mark" x="24" y="60" font-size="34">K&amp;M</text>
    <text class="tag" font-size="8.5"><tspan x="122" y="39">Electrical</tspan><tspan x="122" y="50">Refrigeration</tspan><tspan x="122" y="61">Building Services</tspan></text>
    <text class="addr-h" x="21" y="97" font-size="12">Address :</text>
    <text class="addr" font-size="8"><tspan x="21" y="109">42 Ridge Rd, PO Box 310,</tspan><tspan x="21" y="120">Red Gum NT. 0870</tspan></text>
    <path class="ochre-line" d="M0,122 C150,188 350,218 589,220" stroke-width="3"/>
    <path class="navy" d="M0,131 C150,197 350,226 589,228 L589,257 L0,257 Z"/>
  </g>

  <!-- DL envelope back -->
  <g class="envelope-back" transform="translate(823 340)">
    <rect class="paper" width="589" height="258"/>
    <polyline class="faint-line" points="8,252 292,128 581,252"/>
    <path class="navy" d="M6,0 L589,0 L589,80 Q589,90 579,90 L16,90 Q6,90 6,80 Z"/>
  </g>

  <!-- Meeting minutes -->
  <g class="sheet minutes-sheet" transform="translate(34 573)">
    <rect class="paper" width="338" height="478"/>
    <use href="#sheet-ghost"/>
    <use href="#sheet-head"/>
    <text class="doc-title" x="61" y="108">MEETING MINUTES</text>
    <g class="minutes-table" transform="translate(61 115)">
      <rect class="cell" width="215" height="297"/>
      <line class="cell" x1="42" y1="0" x2="42" y2="54"/>
      <line class="cell" x1="0" y1="13" x2="215" y2="13"/>
      <line class="cell" x1="0" y1="27" x2="215" y2="27"/>
      <line class="cell" x1="0" y1="40" x2="215" y2="40"/>
      <text class="cell-text"><tspan x="4" y="9">Project Name</tspan><tspan x="4" y="23">TOPIC</tspan><tspan x="4" y="36">LOCATION</tspan><tspan x="4" y="50">DATE / TIME</tspan></text>
      <text class="cell-text"><tspan x="46" y="9">Choose Your Name</tspan><tspan x="46" y="23">Deciding concept</tspan><tspan x="46" y="36">Office</tspan><tspan x="46" y="50">19.02.17 / 09:00 - 11:00</tspan></text>
      <rect class="navy" x="0" y="55" width="215" height="14"/>
      <text class="bar-text" x="107" y="64" text-anchor="middle">ATTENDANCE LIST</text>
      <line class="cell" x1="0" y1="84" x2="215" y2="84"/>
      <line class="cell" x1="0" y1="99" x2="215" y2="99"/>
      <line class="cell" x1="0" y1="114" x2="215" y2="114"/>
      <line class="cell" x1="43" y1="69" x2="43" y2="129"/>
      <line class="cell" x1="106" y1="69" x2="106" y2="129"/>
      <line class="cell" x1="150" y1="69" x2="150" y2="129"/>
      <line class="cell" x1="185" y1="69" x2="185" y2="129"/>
      <text class="cell-text" text-anchor="middle"><tspan x="21" y="79">TITLE</tspan><tspan x="74" y="79">NAME</tspan><tspan x="128" y="79">ATTENDANCE</tspan><tspan x="167" y="79">Absence</tspan><tspan x="200" y="79">Note</tspan></text>
      <text class="cell-text" text-anchor="middle"><tspan x="21" y="94">TOPIC # 1</tspan><tspan x="21" y="109">TOPIC # 2</tspan><tspan x="21" y="124">TOPIC # 3</tspan></text>
      <text class="cell-text" text-anchor="middle"><tspan x="72" y="94">TOPIC # 1</tspan><tspan x="72" y="109">TOPIC # 2</tspan><tspan x="72" y="124">TOPIC # 3</tspan></text>
      <text class="cell-text" text-anchor="middle"><tspan x="125" y="94">0</tspan><tspan x="125" y="109">0</tspan><tspan x="125" y="124">0</tspan></text>
      <rect class="navy" x="0" y="129" width="215" height="16"/>
      <text class="bar-text" x="107" y="139" text-anchor="middle">TOPIC S</text>
      <line class="cell" x1="42" y1="145" x2="42" y2="191"/>
      <line class="cell" x1="0" y1="160" x2="215" y2="160"/>
      <line class="cell" x1="0" y1="175" x2="215" y2="175"/>
      <text class="cell-text" text-anchor="middle"><tspan x="21" y="155">1</tspan><tspan x="21" y="170">2</tspan><tspan x="21" y="185">3</tspan></text>
      <rect class="navy" x="0" y="192" width="215" height="17"/>
      <text class="bar-text" x="107" y="202" text-anchor="middle">CONCLUSION</text>
      <rect class="navy" x="0" y="258" width="215" height="17"/>
      <text class="bar-text" x="107" y="269" text-anchor="middle">NEXT MEETING TOPIC</text>
    </g>
    <use href="#sheet-foot"/>
  </g>

  <!-- Internal agenda -->
  <g class="sheet agenda-sheet" transform="translate(424 573)">
    <rect class="paper" width="338" height="478"/>
    <use href="#sheet-ghost"/>
    <use href="#sheet-head"/>
    <text class="doc-title" x="176" y="120" text-anchor="middle">MEETING AGENDA</text>
    <use href="#agenda-body"/>
    <use href="#sheet-foot"/>
  </g>

  <!-- Presentation folder -->
  <g class="folder">
    <path class="charcoal" d="M865,985 L1117,985 L1117,1005 C1112,1060 1105,1100 1097,1115 L878,1115 C868,1095 865,1050 865,985 Z"/>
    <path class="charcoal" d="M1120,985 L1347,985 L1347,1100 C1347,1110 1342,1115 1332,1115 L1145,1115 C1133,1095 1124,1050 1120,1005 Z"/>
    <rect class="charcoal" x="823" y="645" width="22" height="340"/>
    <rect class="charcoal" x="1390" y="645" width="22" height="340"/>
    <circle fill="var(--backdrop)" cx="823" cy="858" r="9"/>
    <circle fill="var(--backdrop)" cx="1412" cy="858" r="9"/>
    <text class="mark-light" font-size="9" transform="translate(831 758) rotate(90)">K&amp;M</text>
    <text class="mark-light" font-size="9" transform="translate(1405 778) rotate(-90)">K&amp;M</text>
    <rect class="navy" x="845" y="645" width="272" height="340"/>
    <text class="ghost-light" x="981" y="840" font-size="70" text-anchor="middle" style="fill:#000;opacity:.07">K&amp;M</text>
    <text class="addr-light" font-size="8.5" x="855" y="920" style="font-weight:700">Address :</text>
    <text class="addr-light" font-size="5.2"><tspan x="855" y="929">42 Ridge Rd, PO Box 310,</tspan><tspan x="855" y="937">Red Gum NT. 0870</tspan></text>
    <rect class="icon-light" x="857" y="944" width="4" height="6.5" rx="0.6"/>
    <text class="addr-light" font-size="5.2" x="869" y="950">Ph: 08 8100 2345</text>
    <rect x="856" y="956" width="6.5" height="5" fill="var(--paper)"/>
    <text class="addr-light" font-size="5.2" x="869" y="962">Fax: 08 8100 2346</text>
    <rect class="icon-light" x="856" y="968" width="7" height="5"/>
    <polyline class="icon-light" points="856,968 859.5,971 863,968"/>
    <text class="addr-light" font-size="5.2" x="869" y="974">info@km.com.au</text>
    <rect class="paper" x="1117" y="645" width="273" height="340"/>
    <text class="mark" x="1142" y="762" font-size="36">K&amp;M</text>
    <text class="tag" font-size="9.5"><tspan x="1259" y="740">Electrical</tspan><tspan x="1259" y="752">Refrigeration</tspan><tspan x="1259" y="764">Building Services</tspan></text>
    <path class="ochre-line" d="M1117,828 C1160,895 1250,918 1390,922" stroke-width="3"/>
    <path class="navy" d="M1117,838 C1162,903 1252,926 1390,930 L1390,985 L1117,985 Z"/>
  </g>

  <!-- CD label -->
  <g class="disc">
    <circle class="navy" cx="222" cy="1315" r="147"/>
    <g clip-path="url(#disc-clip)">
      <path class="paper" d="M60,1258 C150,1236 300,1232 380,1250 L380,1160 L60,1160 Z"/>
      <path class="ochre-line" d="M60,1262 C150,1240 300,1236 380,1254"/>
    </g>
    <text class="ghost-light" x="222" y="1360" font-size="95" text-anchor="middle" style="fill:#000;opacity:.08">K&amp;M</text>
    <text class="mark" x="168" y="1232" font-size="22">K&amp;M</text>
    <text class="tag"><tspan x="234" y="1218">Electrical</tspan><tspan x="234" y="1225">Refrigeration</tspan><tspan x="234" y="1232">Building Services</tspan></text>
    <circle cx="222" cy="1315" r="46" fill="#0d0d0d"/>
    <circle cx="222" cy="1315" r="40" fill="#f2f2f2"/>
    <circle cx="222" cy="1315" r="16" fill="#c8c8c8"/>
    <circle cx="222" cy="1315" r="8" fill="#f7f7f7"/>
  </g>

  <!-- C5 envelope -->
  <g class="envelope-c5" transform="translate(407 1163)">
    <rect class="paper" y="55" width="344" height="244"/>
    <path class="navy" d="M6,0 L338,0 Q344,0 344,6 L344,58 L0,58 L0,6 Q0,0 6,0 Z"/>
    <text class="ghost" x="255" y="230" font-size="95" text-anchor="middle">K&amp;M</text>
    <text class="mark" x="20" y="101" font-size="26">K&amp;M</text>
    <text class="tag" font-size="6"><tspan x="96" y="85">Electrical</tspan><tspan x="96" y="93">Refrigeration</tspan><tspan x="96" y="101">Building Services</tspan></text>
    <path class="ochre-line" d="M0,190 C75,226 195,244 344,244" stroke-width="3"/>
    <path class="navy" d="M0,198 C75,234 195,252 344,252 L344,299 L0,299 Z"/>
    <text class="addr-light" font-size="8.5" x="9" y="263" style="font-weight:700">Address :</text>
    <text class="addr-light" font-size="5.5"><tspan x="9" y="272">42 Ridge Rd, PO Box 310,</tspan><tspan x="9" y="280">Red Gum NT. 0870</tspan></text>
    <rect class="icon-light" x="10" y="288" width="4" height="6.5" rx="0.6"/>
    <text class="addr-light" font-size="5.5" x="21" y="294">Ph: 08 8100 2345</text>
    <rect x="83" y="289" width="6.5" height="5" fill="var(--paper)"/>
    <text class="addr-light" font-size="5.5" x="97" y="294">Fax: 08 8100 2346</text>
    <rect class="icon-light" x="165" y="289" width="7" height="5"/>
    <polyline class="icon-light" points="165,289 168.5,292 172,289"/>
    <text class="addr-light" font-size="5.5" x="178" y="294">info@km.com.au</text>
  </g>

  <!-- Business card front -->
  <g class="card-front" transform="translate(822 1238)">
    <rect class="paper" width="313" height="179"/>
    <path class="navy" d="M0,0 L313,0 L313,24 C230,4 110,2 0,20 Z"/>
    <text class="mark" x="38" y="66" font-size="33">K&amp;M</text>
    <text class="tag" font-size="8"><tspan x="136" y="44">Electrical</tspan><tspan x="136" y="54">Refrigeration</tspan><tspan x="136" y="64">Building Services</tspan></text>
    <text class="mark" x="220" y="101" font-size="20" text-anchor="middle">Sam K &amp; M</text>
    <text class="letter-text" x="220" y="110" font-size="4.6" text-anchor="middle">CORPORATE SERVICES MANAGER</text>
  </g>

  <!-- Business card back -->
  <g class="card-back" transform="translate(1160 1238)">
    <rect class="navy" width="313" height="179"/>
    <path class="ochre-line" d="M0,34 C90,14 220,12 313,40" stroke-width="2.5"/>
    <path class="ochre-line" d="M0,146 C90,168 220,168 313,146" stroke-width="2.5"/>
    <text class="mark-light" x="84" y="102" font-size="33">K&amp;M</text>
    <text class="tag-light" font-size="8.5"><tspan x="176" y="80">Electrical</tspan><tspan x="176" y="91">Refrigeration</tspan><tspan x="176" y="102">Building Services</tspan></text>
  </g>
</svg>
</body>
</html>
```